wolterhagen.info (Physiotherapeut)   //   quellbrand-athletic Webseite
wolterhagen.info (Physiotherapeut) // quellbrand-athletic Webseite
Zielgruppe
Die angesprochene Zielgruppe ist sportlich unterwegs (Sportler jeglicher Sportrichtung). Der externe Shop geht in Richtung Apparels / Kleidung.
Vielleicht wird es aber auch nur eine Physio-Seite und die Apparels kommen im zweiten Schritt - das liegt am Design das man mir präsentiert .... Also legt los ...
(KELVARO wird HOST)
Aufgabenstellung
Mein Name ist Jonathan Wolterhagen ich bin Physiotherapeut / Osteopath (etc).
Die Domain www.wolterhagen.info gehört mir und es würde auch für den Anfang reichen eine digitale Visitenkarte von mir zu erstellen ...
Weiter möchte ich eine Webseite mit dem Namen "quellbrand-athletic" eröffnen. [COM/DE]
Die zu kreierenden Seiten innerhalb der Domain quellbrand-athleti sind:
Main-/LandingPage,
ShopPage (Weiterleitung zu einer externen Webseite),
Impressum,
KooperationsPage (andere Projekte bzw. Webseiten von mir, die in Zukunft kommen).
Design-Vorschläge und umsetzbare / hochladbare Pages (KELVARO) oder NUR Grafiken sind gerne gesehen ...
Die angesprochene Zielgruppe ist sportlich unterwegs (Sportler jeglicher Sportrichtung). Der externe Shop geht in Richtung Apparels.
Die angesprochenen Kreaturen brauchen ein Heim, dass durch ein Schloss repräsentiert werden soll. Evtl. ein Labor. Nicht zu kindlich! Nicht zu düster oder blutig.
Was ich möchte ist: Corporate Identity, eine Webpage (host der Domain wird KELVARO), Logo, etc
Zweiter Schritt wird sein: Grafiken für die Apparels / Klamotten.

```html
<!DOCTYPE html>
<html lang="en">
<head>
<meta charset="utf-8">
<title>Wolterhagen – Main</title>
<link rel="stylesheet" href="https://fonts.googleapis.com/css2?family=Source+Sans+3:wght@400;600;700&display=swap">
<style>
  :root {
    --brand-dark: #3b6a0e;
    --brand-green: #86c540;
    --nav-line: #9fd46a;
    --text-white: #ffffff;
    --footer-text: #3f6d12;
    --copy-text: #eaf6da;
    --figure-tint: #d9efd0;
    --link-blue: #1a33d6;
  }
  * { box-sizing: border-box; margin: 0; padding: 0; }
  html, body { width: 1200px; height: 1145px; overflow: hidden; background: #fff; }
  body { font-family: "Source Sans 3", "Myriad Pro", sans-serif; position: relative; }

  .site-header { position: absolute; left: 0; top: 0; width: 1200px; height: 234px; background: #fff; overflow: hidden; }
  .header-figure { position: absolute; top: 0; height: 234px; }
  .header-figure--left { left: 0; width: 285px; background: linear-gradient(100deg, var(--figure-tint) 0%, rgba(217,239,208,.6) 55%, rgba(255,255,255,0) 100%); }
  .header-figure--right { right: 0; width: 255px; background: linear-gradient(260deg, var(--figure-tint) 0%, rgba(217,239,208,.6) 55%, rgba(255,255,255,0) 100%); }

  .brand { position: absolute; left: 461px; top: 45px; display: flex; align-items: center; gap: 24px; }
  .brand-mark { width: 90px; height: 90px; border-radius: 50%; background: var(--brand-dark); }
  .brand-name { font-size: 31px; font-weight: 400; color: var(--brand-dark); letter-spacing: .3px; }

  .lang-switch { position: absolute; left: 961px; top: 68px; width: 54px; height: 15px; background: var(--brand-dark); display: flex; align-items: center; gap: 5px; padding-left: 4px; }
  .lang-flag { width: 12px; height: 8px; background: #e9e9f1; border-top: 3px solid #c23a3a; }
  .lang-label { font-size: 7.5px; color: #fff; }

  .social { position: absolute; display: flex; align-items: center; gap: 3px; }
  .social-label { font-size: 6.5px; color: var(--brand-dark); margin-right: 3px; }
  .social-icon { width: 12px; height: 12px; border-radius: 2px; }
  .social-icon--a { background: #3b5b9c; }
  .social-icon--b { background: #4aa7e0; }
  .social-icon--c { background: #d3452f; }
  .social-icon--d { background: #6b5546; }
  .social--header { left: 924px; top: 95px; }

  .main-nav { position: absolute; left: 427px; top: 181px; width: 348px; height: 20px; border-bottom: 2px solid var(--nav-line); }
  .main-nav a { position: absolute; top: 0; font-size: 13.5px; color: var(--brand-dark); text-decoration: none; }
  .main-nav a.is-active { font-weight: 700; }

  .content-band { position: absolute; left: 0; top: 234px; width: 1200px; height: 348px; background: var(--brand-green); }
  .intro { position: absolute; left: 182px; top: 41px; width: 419px; color: var(--text-white); font-size: 12.6px; line-height: 16.2px; text-align: justify; }
  .intro p + p { margin-top: 16px; }
  .news { position: absolute; left: 688px; top: 48px; width: 333px; color: var(--text-white); }
  .news-item + .news-item { margin-top: 10px; }
  .news-title { font-size: 12.5px; font-weight: 700; line-height: 16px; }
  .news-body { font-size: 7.6px; line-height: 10.8px; text-align: justify; }

  .hero-photo { position: absolute; left: 0; top: 582px; width: 1200px; height: 379px;
    background: linear-gradient(180deg, #a8d6ea 0%, #b79a86 30%, #8b6f61 55%, #4e3a31 80%, #3a2a24 100%); }

  .site-footer { position: absolute; left: 0; top: 961px; width: 1200px; height: 184px; background: var(--brand-green); }
  .footer-nav { position: absolute; left: 333px; top: 77px; list-style: none; }
  .footer-nav li { font-size: 8px; line-height: 15.8px; color: var(--footer-text); }
  .copyright { position: absolute; left: 433px; top: 76px; width: 334px; font-size: 5.4px; line-height: 8px; color: var(--copy-text); text-align: justify; }
  .contact { position: absolute; left: 785px; top: 82px; font-size: 7.8px; line-height: 11px; color: var(--footer-text); font-style: normal; }
  .contact-heading { margin-bottom: 2px; }
  .contact a { color: var(--link-blue); }
  .social--footer { left: 785px; top: 141px; }
</style>
</head>
<body>
  <header class="site-header">
    <div class="header-figure header-figure--left" role="img" aria-label="Faint green anatomical illustration of running figures"></div>
    <div class="header-figure header-figure--right" role="img" aria-label="Faint green anatomical illustration of a muscular figure"></div>

    <div class="brand">
      <span class="brand-mark"></span>
      <span class="brand-name">Wolterhagen</span>
    </div>

    <div class="lang-switch"><span class="lang-flag"></span><span class="lang-label">English</span></div>

    <div class="social social--header">
      <span class="social-label">Follow Us</span>
      <span class="social-icon social-icon--a"></span>
      <span class="social-icon social-icon--b"></span>
      <span class="social-icon social-icon--c"></span>
      <span class="social-icon social-icon--d"></span>
    </div>

    <nav class="main-nav">
      <a class="is-active" href="#" style="left:0">Main</a>
      <a href="#" style="left:57px">News</a>
      <a href="#" style="left:123px">Shop</a>
      <a href="#" style="left:191px">Contacts</a>
      <a href="#" style="left:276px">Cooperation</a>
    </nav>
  </header>

  <section class="content-band">
    <div class="intro">
      <p>Lorem ipsum dolor sit amet, consectetur adipiscing elit, sed do eiusmod tempor incididunt ut labore et dolore magna aliqua. Ut enim ad minim veniam, quis nostrud exercitation ullamco laboris nisi ut aliquip ex ea commodo consequat. Duis aute irure dolor in reprehenderit in voluptate velit esse cillum dolore eu fugiat nulla pariatur. Excepteur sint occaecat cupidatat non proident, sunt in culpa qui officia deserunt mollit anim id est laborum.</p>
      <p>Lorem ipsum dolor sit amet, consectetur adipiscing elit, sed do eiusmod tempor incididunt ut labore et dolore magna aliqua. Ut enim ad minim veniam, quis nostrud exercitation ullamco laboris nisi ut aliquip ex ea commodo consequat. Duis aute irure dolor in reprehenderit in voluptate velit esse cillum dolore eu fugiat nulla pariatur. Excepteur sint occaecat cupidatat non proident, sunt in culpa qui officia deserunt mollit anim id est laborum.</p>
    </div>
    <div class="news">
      <article class="news-item">
        <h2 class="news-title">Latest News</h2>
        <p class="news-body">Lorem ipsum dolor sit amet, consectetur adipiscing elit, sed do eiusmod tempor incididunt ut labore et dolore magna aliqua. Ut enim ad minim veniam, quis nostrud exercitation ullamco laboris nisi ut aliquip ex ea commodo consequat. Duis aute irure dolor in reprehenderit in voluptate velit esse cillum dolore eu fugiat nulla pariatur. Excepteur sint occaecat cupidatat non proident, sunt in culpa qui officia deserunt mollit anim id est laborum.</p>
      </article>
      <article class="news-item">
        <h2 class="news-title">Latest News</h2>
        <p class="news-body">Lorem ipsum dolor sit amet, consectetur adipiscing elit, sed do eiusmod tempor incididunt ut labore et dolore magna aliqua. Ut enim ad minim veniam, quis nostrud exercitation ullamco laboris nisi ut aliquip ex ea commodo consequat. Duis aute irure dolor in reprehenderit in voluptate velit esse cillum dolore eu fugiat nulla pariatur. Excepteur sint occaecat cupidatat non proident, sunt in culpa qui officia deserunt mollit anim id est laborum. Lorem ipsum dolor sit amet, consectetur adipiscing elit, sed do eiusmod tempor incididunt ut labore et dolore magna aliqua. Ut enim ad minim veniam, quis nostrud exercitation ullamco laboris nisi ut aliquip ex ea commodo consequat. Duis aute irure dolor in reprehenderit in voluptate velit esse cillum dolore eu fugiat nulla pariatur. Excepteur sint</p>
      </article>
    </div>
  </section>

  <div class="hero-photo" role="img" aria-label="Photo of an athlete in a lime green vest sprinting toward the viewer in front of blurred desert mountains under a blue sky"></div>

  <footer class="site-footer">
    <ul class="footer-nav">
      <li>Main</li>
      <li>News</li>
      <li>Shop</li>
      <li>Contacts</li>
      <li>Cooperation</li>
    </ul>
    <p class="copyright">Copyright information. Copyright information. Copyright information. Copyright information. Copyright information. Copyright information. Copyright information. Copyright information. Copyright information. Copyright information. Copyright information. Copyright information. Copyright information. Copyright information. Copyright information. Copyright information. Copyright information. Copyright information. Copyright information. Copyright information. Copyright information. Copyright information. Copyright information. Copyright information. Copyright information. Copyright information. Copyright information. Copyright information. Copyright information. Copyright information. Copyright information. Copyright information. Copyright information. Copyright information. Copyright information. Copyright information. Copyright information. Copyright information. Copyright information. Copyright information. Copyright information. Copyright information. Copyright information. Copyright information. Copyright information.</p>
    <address class="contact">
      <div class="contact-heading">Contact Us</div>
      <div>Lindenweg 14</div>
      <div>26135 Feldhausen</div>
      <div>Tel: +49 (0)441 555-0182</div>
      <div>E-mail: <a href="#">info@wolterhagen.info</a></div>
    </address>
    <div class="social social--footer">
      <span class="social-label">Follow Us</span>
      <span class="social-icon social-icon--a"></span>
      <span class="social-icon social-icon--b"></span>
      <span class="social-icon social-icon--c"></span>
      <span class="social-icon social-icon--d"></span>
    </div>
  </footer>
</body>
</html>
```